Modern business card for triathlon training business in Australia

We need a business card design for our triathlon training company.

Pace with Us Fitness is an Australian business, owned by women, run for women. Pace with Us Fitness helps women prepare or improve triathlon skills and confidence through triathlon camps completely designed for women.

Our camps focus on preparing women both physically and mentally for their next (or first!) triathlon.

You can see our website www.pacewithusfitness.com.au for more info about our business and our style.

We've attached two of our logos and are happy to consider a design that utilised either colour scheme with the teal colour being our 'feature' colour. We don't want overly feminine cards but rather cards that are professional and neat. If the inclusion of any pictures/art is warranted, this should be focused on our swim/ride/run theme and in that specific order (swim/ride/run).

The business card needs to be a printable design and the contact details will need to change for our two employees.

Target Market(s)

Female clients and partners/vendors/sponsors that we work with in the triathlon industry

Industry/Entity Type

Fitness

Contact Information for Business Card

Pace with Us Fitness (business name)
Nina Carver
Business Director
Mobile: 0438 916 207
Email: nina@pacewithusfitness.com.au
www.pacewithusfitness.com.au

Second business card:
Pace with Us Fitness
Bel Stray
Coaching Director
Mobile: 0459 260 718
Email: bel@pacewithusfitness.com.au

Font styles to use
Serif
Sans Serif

Requirements
Must have
• Core contact details above, our logo and be a printable design
Should not have
• Pink
• Cursive/script fonts

```html
<!DOCTYPE html>
<html lang="en">
<head>
<meta charset="utf-8">
<title>Pace with Us Fitness — Business Cards</title>
<link href="https://fonts.googleapis.com/css2?family=Montserrat:wght@700;800&family=Open+Sans:wght@400;600&display=swap" rel="stylesheet">
<style>
  :root {
    --canvas: #e8edef;
    --charcoal: #3b3c3e;
    --paper: #f4f5f6;
    --teal-deep: #167f8c;
    --teal: #2a9aa6;
    --teal-light: #5cb9c2;
    --cyan: #2cc6d6;
    --silver: #b9bfc3;
    --white: #ffffff;
  }
  * { box-sizing: border-box; margin: 0; padding: 0; }
  html, body {
    width: 1200px;
    height: 1000px;
    overflow: hidden;
    background: var(--canvas);
  }
  .sheet {
    position: relative;
    width: 1200px;
    height: 1000px;
  }
  .card {
    position: absolute;
    left: 220px;
    width: 760px;
    height: 434px;
    overflow: hidden;
    box-shadow: 0 10px 28px rgba(0, 0, 0, 0.18);
  }
  .card--business { top: 50px; background: var(--charcoal); }
  .card--coaching { top: 516px; background: var(--paper); }
  .card__art {
    position: absolute;
    inset: 0;
    width: 760px;
    height: 434px;
  }
  .brand {
    position: absolute;
    left: 36px;
    bottom: 46px;
  }
  .brand__name {
    font-family: "Montserrat", sans-serif;
    font-weight: 700;
    font-size: 21px;
    line-height: 1.1;
    letter-spacing: 0.3px;
    text-transform: uppercase;
    white-space: nowrap;
    color: var(--cyan);
  }
  .brand__web {
    margin-top: 6px;
    font-family: "Open Sans", sans-serif;
    font-weight: 600;
    font-size: 13px;
    white-space: nowrap;
    color: var(--cyan);
  }
  .card--coaching .brand__web { color: var(--teal); }
  .person {
    position: absolute;
    left: 500px;
    top: 78px;
    color: var(--white);
  }
  .person__name {
    font-family: "Montserrat", sans-serif;
    font-weight: 800;
    font-size: 24px;
    letter-spacing: 0.5px;
    text-transform: uppercase;
    white-space: nowrap;
  }
  .person__role {
    margin-top: 2px;
    font-family: "Montserrat", sans-serif;
    font-weight: 700;
    font-size: 10px;
    letter-spacing: 1px;
    text-transform: uppercase;
  }
  .contact {
    position: absolute;
    left: 400px;
    top: 330px;
    font-family: "Open Sans", sans-serif;
    font-size: 14px;
    line-height: 1.6;
    white-space: nowrap;
    color: var(--white);
  }
</style>
</head>
<body>
<main class="sheet">

  <article class="card card--business">
    <svg class="card__art" viewBox="0 0 760 434" aria-hidden="true">
      <defs>
        <linearGradient id="tealPanel" x1="0" y1="0" x2="1" y2="0.4">
          <stop offset="0" stop-color="#167f8c"/>
          <stop offset="0.55" stop-color="#2a9aa6"/>
          <stop offset="1" stop-color="#1c8794"/>
        </linearGradient>
      </defs>
      <polygon points="520,0 760,0 760,434 300,434" fill="url(#tealPanel)"/>
      <polygon points="700,0 716,0 604,220 588,220" fill="#b9bfc3"/>
      <polygon points="716,0 760,0 760,60 679,220 604,220" fill="#2cc6d6"/>
    </svg>
    <div class="brand">
      <p class="brand__name">Pace with Us Fitness</p>
      <p class="brand__web">www.pacewithusfitness.com.au</p>
    </div>
    <div class="person">
      <p class="person__name">Nina Carver</p>
      <p class="person__role">Business Director</p>
    </div>
    <div class="contact">
      <p>Email: nina@pacewithusfitness.com.au</p>
      <p>Mobile: 0438 916 207</p>
    </div>
  </article>

  <article class="card card--coaching">
    <svg class="card__art" viewBox="0 0 760 434" aria-hidden="true">
      <defs>
        <linearGradient id="tealPanelLight" x1="0" y1="0" x2="1" y2="0.4">
          <stop offset="0" stop-color="#167f8c"/>
          <stop offset="0.4" stop-color="#5cb9c2"/>
          <stop offset="0.7" stop-color="#2a9aa6"/>
          <stop offset="1" stop-color="#1c8794"/>
        </linearGradient>
      </defs>
      <polygon points="520,0 760,0 760,434 300,434" fill="url(#tealPanelLight)"/>
      <polygon points="700,0 716,0 604,220 588,220" fill="#b9bfc3"/>
      <polygon points="716,0 760,0 760,60 679,220 604,220" fill="#2cc6d6"/>
    </svg>
    <div class="brand">
      <p class="brand__name">Pace with Us Fitness</p>
      <p class="brand__web">www.pacewithusfitness.com.au</p>
    </div>
    <div class="person">
      <p class="person__name">Bel Stray</p>
      <p class="person__role">Coaching Director</p>
    </div>
    <div class="contact">
      <p>Email: bel@pacewithusfitness.com.au</p>
      <p>Mobile: 0459 260 718</p>
    </div>
  </article>

</main>
</body>
</html>
```